KOV Auto Electrical, Auto Parts Needs An High End Business Card Design

I have just undergone a re-branding and changing to a PTY LTD for my business I have also started another sister business to compliment my current business. I want to stick with the basis of my logo design as people associate it with my business but I just want to refine it. I want the business card to look professional and organised. I would like to have my company details on the card such as Email, Web Address, License No, ACN and ABN, Phone.

Target Market(s)

Mining, Automotive, Travellers, Car Enthusiasts

Industry/Entity Type

Business

Contact Information for Business Card

So I am basically after 3 logo's.

First one is "KOV Group"
Second Business Name is "KOV Auto Electrical"
Thirs business name is "KOV Auto Parts"

I want to use my current logo for the KOV part of each business name I will attach file and but I don't mind if the colour is changed.

I would like KOV Group to appear on both side of the business card and then I want KOV Auto Electrical to appear on one side and KOV Auto Parts to appear on the other

My business is an Automotive Electrical Business and my other business sells automotive electrical parts.

On KOV Auto Electrical Side.
Dylan Mercer
Mob: 0417 286 534
Email: dylanm@kovelectrical.example.com.au
www.KOVElectrical.example.com.au
www.facebook.com/KOVElectricalExample
MVRL72648
AU58217

On KOV Auto Parts side
Dylan Mercer
Mob: 0417 286 534
Email: dylanm@kovautoparts.example.com.au
www.KOVAutoParts.example.com.au

Requirements
Must have
• Professional Look,
Nice to have
• Isometric feel.
Should not have
• Informal fonts

```html
<!DOCTYPE html>
<html lang="en">
<head>
<meta charset="utf-8">
<title>KOV Group Business Card</title>
<link rel="stylesheet" href="https://fonts.googleapis.com/css2?family=Lato:wght@400;700;900&display=swap">
<style>
  :root {
    --backdrop: #dcdcdc;
    --card-white: #ffffff;
    --card-black: #0c0c0c;
    --ink: #111111;
    --ink-light: #ffffff;
    --brand-yellow: #f5ec1f;
    --rule-yellow: #f1e84a;
  }
  * { box-sizing: border-box; margin: 0; padding: 0; }
  html, body { width: 1200px; height: 926px; overflow: hidden; }
  body {
    background: var(--backdrop);
    font-family: "Lato", Arial, sans-serif;
    color: var(--ink);
    display: grid;
    grid-template-columns: 560px 560px;
    grid-template-rows: 320px 320px;
    column-gap: 30px;
    row-gap: 50px;
    justify-content: center;
    align-content: center;
  }
  .card {
    width: 560px;
    height: 320px;
    position: relative;
    box-shadow: 0 6px 18px rgba(0,0,0,0.18);
    overflow: hidden;
  }
  .card-front { background: var(--card-white); }
  .card-parts { background: var(--card-black); color: var(--ink-light); }
  .card-logo {
    background: var(--card-black);
    grid-column: 1 / span 2;
    justify-self: center;
    display: flex;
    align-items: center;
    justify-content: center;
  }
  .brand-name {
    font-weight: 900;
    color: var(--brand-yellow);
    letter-spacing: 2px;
    line-height: 1;
  }
  .card-front .brand-name {
    position: absolute;
    left: 27px;
    top: 20px;
    font-size: 66px;
  }
  .card-logo .brand-name { font-size: 160px; letter-spacing: 5px; }
  .holder {
    position: absolute;
    right: 29px;
    top: 94px;
    text-align: right;
  }
  .holder-name {
    font-size: 22px;
    font-weight: 700;
    letter-spacing: 2.5px;
    text-transform: uppercase;
  }
  .holder-phone {
    margin-top: 8px;
    font-size: 16px;
    font-weight: 700;
    letter-spacing: 1.2px;
    display: inline-flex;
    align-items: center;
    gap: 7px;
  }
  .card-parts .holder-phone { color: var(--brand-yellow); }
  .contact-block {
    position: absolute;
    display: flex;
    flex-direction: column;
    gap: 5px;
    font-size: 11.5px;
    font-weight: 700;
  }
  .contact-electrical { left: 24px; top: 170px; }
  .contact-parts { right: 29px; top: 200px; }
  .parts-side { right: 29px; top: 168px; }
  .side-title { font-size: 17px; font-weight: 700; margin-bottom: 3px; }
  .contact-row { display: flex; align-items: center; gap: 7px; }
  .contact-row svg { flex: none; }
  .divider {
    position: absolute;
    left: 0;
    right: 0;
    height: 2px;
    background: var(--rule-yellow);
  }
  .card-front .divider { top: 242px; }
  .card-parts .divider { top: 256px; }
  .company-details {
    position: absolute;
    left: 0;
    right: 0;
    top: 254px;
    text-align: center;
    font-size: 14.5px;
    line-height: 1.4;
  }
</style>
</head>
<body>
  <section class="card card-front">
    <div class="brand-name">KOV</div>

    <div class="holder">
      <div class="holder-name">Dylan Mercer</div>
      <div class="holder-phone">0417 286 534
        <svg width="13" height="19" viewBox="0 0 16 24" aria-hidden="true">
          <rect x="1" y="1" width="14" height="22" rx="2" fill="none" stroke="#111" stroke-width="2"/>
          <line x1="1" y1="18" x2="15" y2="18" stroke="#111" stroke-width="2"/>
        </svg>
      </div>
    </div>

    <div class="contact-block contact-electrical">
      <div class="contact-row">
        <svg width="12" height="12" viewBox="0 0 14 14" aria-hidden="true"><path d="M6 8 L8 6 M5 6 L3 8 a2 2 0 0 0 3 3 L8 9 M9 8 L11 6 a2 2 0 0 0 -3 -3 L6 5" fill="none" stroke="#111" stroke-width="1.6"/></svg>
        dylanm@kovelectrical.example.com.au
      </div>
      <div class="contact-row">
        <svg width="12" height="9" viewBox="0 0 14 11" aria-hidden="true"><rect width="14" height="11" fill="#111"/><path d="M0 0 L7 6 L14 0" fill="none" stroke="#fff" stroke-width="1.2"/></svg>
        www.KOVElectrical.example.com.au
      </div>
    </div>

    <div class="contact-block contact-parts">
      <div class="contact-row">
        <svg width="12" height="12" viewBox="0 0 14 14" aria-hidden="true"><path d="M6 8 L8 6 M5 6 L3 8 a2 2 0 0 0 3 3 L8 9 M9 8 L11 6 a2 2 0 0 0 -3 -3 L6 5" fill="none" stroke="#111" stroke-width="1.6"/></svg>
        dylanm@kovautoparts.example.com.au
      </div>
      <div class="contact-row">
        <svg width="12" height="9" viewBox="0 0 14 11" aria-hidden="true"><rect width="14" height="11" fill="#111"/><path d="M0 0 L7 6 L14 0" fill="none" stroke="#fff" stroke-width="1.2"/></svg>
        www.KOVAutoParts.example.com.au
      </div>
    </div>

    <div class="divider"></div>

    <div class="company-details">
      <p>facebook: www.facebook.com/KOVElectricalExample</p>
      <p>address: MVRL72648 AU58217</p>
    </div>
  </section>

  <section class="card card-parts">
    <div class="holder">
      <div class="holder-name">Dylan Mercer</div>
      <div class="holder-phone">0417 286 534
        <svg width="13" height="19" viewBox="0 0 16 24" aria-hidden="true">
          <rect x="1" y="1" width="14" height="22" rx="2" fill="none" stroke="#f5ec1f" stroke-width="2"/>
          <line x1="1" y1="18" x2="15" y2="18" stroke="#f5ec1f" stroke-width="2"/>
        </svg>
      </div>
    </div>

    <div class="contact-block parts-side">
      <div class="side-title">KOV Auto Parts side</div>
      <div class="contact-row">dylanm@kovautoparts.example.com.au</div>
      <div class="contact-row">www.KOVAutoParts.example.com.au</div>
    </div>

    <div class="divider"></div>
  </section>

  <section class="card card-logo">
    <div class="brand-name">KOV</div>
  </section>
</body>
</html>
```